Agriculture new feeding concept for bull fattening needs a one-page flyer *

We are the innovation leader in the field of cattle feeding in Switzerland. Now we are launching a new “Tarsela” project for cattle fatteners, Munimäster (bull fattening). Tarsela is a complete fattening regime (feed, feed additives, services and advice).
Our sales representatives are with customers every day. You advertise the new project with the aim that our internal specialists get an appointment with the customer for a non-binding presentation of the project. This flyer is intended for this purpose.
Effect:
1. Innovative, modern
2. New
3. emotions
4. technical, scientific

You are also welcome to create a “logo” for Tarsela or choose / design your own lettering.
If you wish to use them, you will also find pictures of such fattening bulls in the appendix. However, pictures are not absolutely necessary.
Size A5, one-sided
Title: TARSELA - for beef fattening professionals
Text:
• Best fattening results
• Top customer service
• Innovative products
• Attractive conditions

Banner or similar:
May we introduce ourselves? or we would be happy to visit you. Etc.

```html
<!DOCTYPE html>
<html lang="de">
<head>
<meta charset="utf-8">
<title>Tarsela – Neues Fütterungskonzept für Bullenmast</title>
<link href="https://fonts.googleapis.com/css2?family=Baloo+2:wght@800&family=Montserrat:wght@500;600;700;800&display=swap" rel="stylesheet">
<style>
  :root {
    --paper: #fce9e3;
    --ink: #111111;
    --peach: #f7b894;
    --salmon: #f4a47c;
    --white: #ffffff;
    --barn-roof: #7d8282;
    --barn-light: #c9c6c0;
    --hide: #a47a4e;
    --hide-dark: #7a5a3a;
    --feed: #b49a6a;
    --floor: #cfc8bd;
  }
  html, body { margin: 0; padding: 0; overflow: hidden; }
  body { width: 846px; height: 1200px; background: var(--paper); }
  .flyer {
    position: relative; width: 846px; height: 1200px; overflow: hidden;
    background: var(--paper); font-family: "Montserrat", Arial, sans-serif; color: var(--ink);
  }
  .hero { position: absolute; left: 0; top: 0; width: 846px; height: 830px; }
  .headline {
    position: absolute; left: 249px; top: 88px; width: 597px; height: 118px;
    background: var(--ink); box-sizing: border-box; padding: 10px 0 0 36px;
    font-family: "Baloo 2", "Arial Rounded MT Bold", sans-serif; font-weight: 800;
    font-size: 43px; line-height: 47px; color: var(--salmon); margin: 0; white-space: nowrap;
  }
  .benefits {
    position: absolute; left: 44px; top: 852px; margin: 0; padding: 0; list-style: none;
    font-size: 26px; font-weight: 600; letter-spacing: 1.2px; line-height: 48px;
  }
  .benefits li::before { content: "•"; margin-right: 12px; }
  .intro {
    position: absolute; left: 434px; top: 852px; width: 360px; margin: 0;
    font-size: 17.5px; font-weight: 500; line-height: 33px;
  }
  .brand { position: absolute; left: 430px; top: 1026px; width: 400px; }
  .brand-name {
    display: flex; align-items: center; gap: 14px;
    font-size: 80px; font-weight: 800; line-height: 80px; letter-spacing: 1px;
  }
  .brand-dot { width: 26px; height: 26px; border-radius: 50%; background: var(--ink); }
  .brand-tagline { font-size: 17px; font-weight: 600; letter-spacing: 0.4px; margin-top: 4px; }
  .web {
    position: absolute; left: 0; top: 1098px; width: 394px; height: 44px;
    background: var(--peach); border-radius: 0 22px 22px 0;
    font-size: 18px; font-weight: 600; letter-spacing: 6px; line-height: 44px;
    box-sizing: border-box; padding-left: 72px;
  }
  .contact {
    position: absolute; left: 0; top: 1145px; width: 846px; height: 55px;
    background: var(--ink); color: var(--white); box-sizing: border-box; padding-left: 66px;
    font-size: 25px; font-weight: 700; letter-spacing: 2px; line-height: 55px; white-space: nowrap;
  }
  .contact .sep { margin: 0 16px; font-weight: 500; }
</style>
</head>
<body>
<main class="flyer">
  <svg class="hero" viewBox="0 0 846 830" xmlns="http://www.w3.org/2000/svg">
    <defs>
      <linearGradient id="barnTone" x1="0.2" y1="0" x2="0.5" y2="1">
        <stop offset="0" stop-color="var(--barn-roof)"/>
        <stop offset="0.25" stop-color="var(--barn-light)"/>
        <stop offset="0.45" stop-color="var(--hide)"/>
        <stop offset="0.62" stop-color="var(--hide-dark)"/>
        <stop offset="0.8" stop-color="var(--feed)"/>
        <stop offset="1" stop-color="var(--floor)"/>
      </linearGradient>
    </defs>
    <circle cx="372" cy="392" r="406" fill="none" stroke="var(--ink)" stroke-width="7"/>
    <circle cx="358" cy="384" r="402" fill="url(#barnTone)" role="img"
            aria-label="Foto: Rinder im hellen Stall fressen am Futtergitter"/>
  </svg>

  <h1 class="headline">Neues Fütterungskonzept<br>für Bullenmast</h1>

  <ul class="benefits">
    <li>Beste Mastergebnisse</li>
    <li>Bester Kundenservice</li>
    <li>Innovative Produkte</li>
    <li>Attraktive Konditionen</li>
  </ul>

  <p class="intro">Unsere Aussendienstmitarbeiter sind täglich bei Kunden, damit unsere Spezialisten einen Termin für eine unverbindliche Präsentation dieses neuen Konzepts erhalten.</p>

  <div class="brand">
    <div class="brand-name"><span>TARSELA</span><span class="brand-dot"></span></div>
    <div class="brand-tagline">CATTLE FATTENERS, MUNIMÄSTER</div>
  </div>

  <div class="web">www.tarsela.de</div>

  <footer class="contact">Contact : 98230145566<span class="sep">|</span>kontakt@tarsela.de</footer>
</main>
</body>
</html>
```